Hello Creative Minds!
Our business is after a elegant and classy flyer that draws attention!
The business is Tallow Brook - Lawn Rejuvenation Services. We provide services that maintain a healthy and vibrant green lawn through the tough Australian seasons. The products we use limits the water needed to keep grass green to a minimum - practically none at all! This not only helps the home owner or home seller but the environment by limiting the use of water that is needed to create a green lawn. The products we use are made from natural ingredients that are and pet friendly.
This fly will be our introductory offer to the market. Below are the required points that need to be on the flyer. Attached is the business logo, before & after pictures and 1 example of the LAYOUT not DESIGN of what the flyer should be laid out like or similar to. Feel free to use different 'Lawn Mower' pictures.
All the best; if you need any questions answered please feel free to message.
REQUIRED POINTS (Please re-phrase were possible);
*Instantly restores the natural green colour of grass – year round
*Lasts for up to 3 months
*Substantially reduces watering needs
*Pet friendly
*Stays green during droughts and water restrictions
*UV fade resistant
*Won’t bleed, run, or stain once absorbed into the grass
*Safe for the environment, pets and people
*Works in extreme heat, cold and frost
*Organic and natural – no harmful chemicals
*Reduces the amount of fertilizer
and water used on lawns
*Kerb appeal is essential for getting your property sold for the highest price possible
SERVICES & PRICING
Lawn maintenance (cut & trim) starting from $60
Lawn rejuvenation starting from $80 (Only $27 a month for 3 months)*
Package deal starting from $120
Introductory offer: 25% off all services. Refer a friend, when they book you receive another 25% off your next service.
LOCATIONS
Nowra to Sydney
CONTACT NUMBER
Will be posted with the winner - please leave an area for this.
SOCIAL MEDIA
Please add Facebook and Instagram logo's
Updates
Competition has finished, thank you to all that have participated! I will review and comment on the flyers that need assistance. All the best with future designs!
Target Market(s)
home owners, home sellers, property developers, real estates and nursing homes and government housing.
Industry/Entity Type
Lawn Care
Look and feel

```html
<!DOCTYPE html>
<html lang="en">
<head>
<meta charset="utf-8">
<title>Tallow Brook - Lawn Rejuvenation Services</title>
<link rel="stylesheet" href="https://fonts.googleapis.com/css2?family=Open+Sans:wght@400;600;700;800&display=swap">
<style>
  :root{
    --bg:#e9e7e3;
    --panel:#2c3036;
    --green:#8cc63f;
    --green-dark:#5f9a22;
    --lime:#a6d84a;
    --white:#ffffff;
    --grey-line:#b9bcc0;
    --tag-grey:#555a60;
  }
  *{box-sizing:border-box;margin:0;padding:0}
  html,body{width:977px;height:1200px;overflow:hidden;background:var(--bg)}
  body{font-family:"Open Sans",Arial,sans-serif;color:var(--white)}
  .flyer{position:relative;width:977px;height:1200px;overflow:hidden;background:var(--panel)}
  .hero-photo{position:absolute;left:0;top:0;width:977px;height:600px;
    background:linear-gradient(180deg,#7d9c4a 0%,#4f8a26 30%,#5aa12b 65%,#2f6a16 100%)}
  .shapes{position:absolute;left:0;top:0;width:977px;height:1200px}
  .grass-strip{position:absolute;left:0;top:1088px;width:977px;height:112px;
    background:linear-gradient(180deg,rgba(44,48,54,0) 0%,#3d7f1d 45%,#2d6a14 100%)}
  .logo{position:absolute;left:30px;top:414px;width:440px;color:var(--green-dark)}
  .logo-name{font-size:60px;font-weight:600;letter-spacing:1px;line-height:1}
  .logo-tag{margin-top:10px;margin-left:58px;font-size:12px;letter-spacing:4px;color:var(--tag-grey);font-weight:600;text-transform:uppercase;white-space:nowrap}
  .photo-circle{position:absolute;border-radius:50%;border:8px solid rgba(255,255,255,.85);box-shadow:0 0 0 6px rgba(255,255,255,.25)}
  .before-after{left:583px;top:265px;width:290px;height:290px;display:flex;overflow:hidden}
  .before-after .half{flex:1;position:relative}
  .before-after .before{background:linear-gradient(160deg,#c9a97a,#9c7d4f)}
  .before-after .after{background:linear-gradient(160deg,#7b8d4f,#4f6b2c);border-left:3px solid var(--white)}
  .before-after .label{position:absolute;top:22px;font-size:18px;font-style:italic;color:var(--white)}
  .before .label{right:18px}.after .label{left:14px}
  .hands{left:499px;top:434px;width:196px;height:196px;background:linear-gradient(160deg,#b9c98a 0%,#6fa83a 50%,#3f7f1e 100%)}
  .mower{left:765px;top:413px;width:196px;height:196px;background:linear-gradient(180deg,#9fd06a 0%,#5aa12b 55%,#3a7a1a 100%)}
  .services{position:absolute;left:35px;top:601px;width:590px}
  .pill-title{display:inline-block;background:var(--green);color:var(--white);font-weight:800;font-size:21px;padding:4px 62px 4px 18px;border-radius:18px}
  .service-list{list-style:none;margin-top:28px}
  .service-list li{position:relative;padding-left:40px;font-size:17.5px;font-weight:600;line-height:21px;margin-bottom:8px}
  .service-list li.tick::before{content:"";position:absolute;left:4px;top:1px;width:19px;height:19px;border-radius:50%;background:var(--green)}
  .service-list li.tick::after{content:"";position:absolute;left:10px;top:5px;width:5px;height:9px;border:solid var(--white);border-width:0 2.5px 2.5px 0;transform:rotate(45deg)}
  .pricing{position:absolute;left:655px;top:647px;width:274px}
  .price-box{border:2px dashed rgba(255,255,255,.75);border-radius:10px;text-align:center;padding:12px 8px;margin-bottom:16px;display:flex;flex-direction:column;justify-content:center}
  .price-box h3{font-size:18px;font-weight:800;text-transform:uppercase;line-height:22px}
  .price-box .note,.price-box .price{color:var(--lime);font-weight:700;font-size:18px;line-height:22px}
  .price-box .fine{color:var(--lime);font-size:11px;font-weight:600}
  .box-maint{height:101px}.box-rejuv{height:97px}.box-package{height:97px}
  .box-offer{height:99px;margin-bottom:0}
  .box-offer .kicker{color:var(--lime);font-size:12px;font-weight:600;text-transform:uppercase}
  .box-offer h3{font-size:20px}
  .box-offer .fine{font-size:10px;line-height:13px;margin-top:3px}
  .estimate{position:absolute;left:196px;top:1115px;width:549px;height:46px;border-radius:23px;background:var(--green);display:flex;align-items:center;justify-content:center;gap:14px;font-weight:800;font-size:24px}
  .estimate .label{font-size:23px;text-transform:uppercase}
  .estimate svg{width:28px;height:28px}
  .website{position:absolute;left:196px;top:1168px;width:549px;text-align:center;font-size:20px;font-weight:800}
  .social{position:absolute;top:1141px;width:40px;height:40px;border-radius:50%;background:var(--green)}
  .social-a{left:48px}.social-b{left:108px}
</style>
</head>
<body>
<main class="flyer">
  <div class="hero-photo" role="img" aria-label="Photo of a hand resting on a lush green lawn"></div>

  <svg class="shapes" viewBox="0 0 977 1200" aria-hidden="true">
    <path d="M0 582 C 220 560 430 520 640 490 C 760 474 880 468 977 466 L977 1200 L0 1200 Z" fill="var(--panel)"/>
    <path d="M0 392 C 180 372 440 368 650 428 C 470 470 250 540 0 590 Z" fill="var(--white)"/>
    <path d="M0 384 C 190 362 450 360 662 426" fill="none" stroke="var(--grey-line)" stroke-width="3"/>
    <path d="M0 598 C 250 548 470 478 662 426" fill="none" stroke="var(--grey-line)" stroke-width="3"/>
  </svg>

  <div class="grass-strip" role="img" aria-label="Photo of green grass blades along the bottom edge"></div>

  <div class="logo">
    <div class="logo-name">Tallow Brook</div>
    <div class="logo-tag">Lawn Rejuvenation Services</div>
  </div>

  <div class="photo-circle before-after">
    <div class="half before" role="img" aria-label="Photo of dry brown lawn before treatment"><span class="label">before</span></div>
    <div class="half after" role="img" aria-label="Photo of green lawn after treatment"><span class="label">after</span></div>
  </div>
  <div class="photo-circle hands" role="img" aria-label="Photo of cupped hands holding fresh grass"></div>
  <div class="photo-circle mower" role="img" aria-label="Photo of a lawn mower on a green lawn"></div>

  <section class="services">
    <h2 class="pill-title">OUR SERVICES</h2>
    <ul class="service-list">
      <li class="tick">Instantly restores the natural green colour of<br>grass – year round</li>
      <li class="tick">Lasts for up to 3 months</li>
      <li class="tick">Substantially reduces watering needs</li>
      <li class="tick">Pet friendly</li>
      <li class="tick">Stays green during droughts and water restrictions</li>
      <li class="tick">UV fade resistant</li>
      <li class="tick">Won't bleed, run, or stain once absorbed into<br>the grass</li>
      <li class="tick">Safe for the environment, pets and people</li>
      <li>Works in extreme heat, cold and frost</li>
      <li class="tick">Organic and natural – no harmful chemicals</li>
      <li class="tick">Reduces the amount of fertilizer<br>and water used on lawns</li>
      <li class="tick">Kerb appeal is essential for getting your property<br>sold for the highest price possible</li>
    </ul>
  </section>

  <section class="pricing">
    <div class="price-box box-maint">
      <h3>Lawn Maintenance</h3>
      <p class="note">(cut &amp; trim)</p>
      <p class="price">starting from $60</p>
    </div>
    <div class="price-box box-rejuv">
      <h3>Lawn Rejuvenation</h3>
      <p class="price">starting from $80</p>
      <p class="fine">(Only $27 a month for 3 months)*</p>
    </div>
    <div class="price-box box-package">
      <h3>Package Deal</h3>
      <p class="price">starting from $120</p>
    </div>
    <div class="price-box box-offer">
      <p class="kicker">Introductory offer:</p>
      <h3>25% off all services</h3>
      <p class="fine">Refer a friend, when they book you receive another 25% off your next service.</p>
    </div>
  </section>

  <span class="social social-a" aria-label="Social media"></span>
  <span class="social social-b" aria-label="Social media"></span>

  <div class="estimate">
    <span class="label">Free Estimate</span>
    <svg viewBox="0 0 28 28" aria-hidden="true">
      <circle cx="14" cy="14" r="12" fill="none" stroke="var(--white)" stroke-width="2.2"/>
      <path d="M10 8.5 l2.3 -0.6 1.3 3.2 -1.6 1.2 c.7 1.6 1.8 2.8 3.4 3.5 l1.2 -1.6 3.2 1.3 -.6 2.3 c-5.4 .2 -9.6 -4 -9.2 -9.3z" fill="var(--white)"/>
    </svg>
    <span class="phone">123 555 0199</span>
  </div>
  <div class="website">www.TallowBrook.com</div>
</main>
</body>
</html>
```